New Property development signage

large poster for a new development.
3 metres x 2 metres. To include the following.

Verrow Gardens
TO LET
LUXURY FULLY FURNISHED LARGE
2 AND 3 BED APARTMENTS
Tallick Estates
362 4105
www.tallickestates-example.com

Need this to be large simple writing with Tallick estates logo on the bottom

Target Market(s)

High end rental property market

Industry/Entity Type

Real Estate Development

Colors
000000
cbcbcb
0555a3

Requirements
Must have
• Name of the development must be in a different font, classic style
Nice to have
• Light Grey background, blues for colours
Should not have
• anymore than 3 /4 colours

```html
<!DOCTYPE html>
<html lang="en">
<head>
<meta charset="utf-8">
<title>Verrow Gardens – To Let – Tallick Estates</title>
<link rel="stylesheet" href="https://fonts.googleapis.com/css2?family=Roboto+Condensed:wght@700&family=Playfair+Display:wght@700&family=Archivo:wdth,wght@125,900&display=swap">
<style>
  :root {
    --brand-blue: #2a5699;
    --ink: #2b2b2b;
    --paper: #ffffff;
    --band-text: #e4e9f2;
    --edge-grey: #d6d6d6;
  }
  * { margin: 0; padding: 0; box-sizing: border-box; }
  html, body { width: 1200px; height: 902px; overflow: hidden; background: var(--paper); }
  .canvas {
    position: relative; width: 1200px; height: 902px;
    border: 2px solid var(--edge-grey);
    font-family: "Roboto Condensed", "Arial Narrow", sans-serif;
    font-weight: 700;
  }
  .sign {
    position: absolute; left: 45px; top: 80px; width: 1105px; height: 737px;
    background: var(--brand-blue);
  }
  .panel {
    position: absolute; left: 18px; width: 1069px; background: var(--paper);
    text-align: center;
  }

  /* Headline panel */
  .headline-panel { top: 18px; height: 160px; display: flex; align-items: center; justify-content: center; }
  .to-let { color: var(--brand-blue); font-size: 128px; line-height: 1; letter-spacing: 4px; }

  /* Services band */
  .services {
    position: absolute; top: 178px; left: 0; width: 100%; height: 50px;
    display: flex; justify-content: center; align-items: center; gap: 46px;
    color: var(--band-text); font-size: 34px;
  }

  /* Offer panel */
  .offer-panel { top: 228px; height: 320px; }
  .development-name {
    color: var(--brand-blue);
    font-family: "Playfair Display", Georgia, serif; font-weight: 700;
    font-size: 64px; margin-top: 22px; line-height: 1.1;
  }
  .offer-sub { color: var(--ink); font-size: 29px; line-height: 1.2; }
  .feature-headline { color: var(--brand-blue); font-size: 46px; margin-top: 20px; line-height: 1.1; }
  .features { color: var(--ink); font-size: 33px; line-height: 1.28; margin-top: 4px; }

  /* Phone band */
  .phone {
    position: absolute; top: 548px; left: 0; width: 100%; height: 90px;
    display: flex; justify-content: center; align-items: center;
    color: var(--paper);
    font-family: "Archivo", "Arial Black", sans-serif; font-stretch: 125%; font-weight: 900;
    font-size: 76px; letter-spacing: 3px;
  }

  /* Brand panel */
  .brand-panel {
    top: 638px; height: 81px;
    display: flex; flex-direction: column; justify-content: center; align-items: center;
  }
  .brand-name { color: var(--brand-blue); font-size: 38px; line-height: 40px; letter-spacing: 6px; }
  .web-address { color: var(--ink); font-size: 30px; line-height: 34px; }
</style>
</head>
<body>
  <div class="canvas">
    <div class="sign">
      <div class="panel headline-panel">
        <p class="to-let">TO LET</p>
      </div>
      <div class="services">
        <span>sales</span><span>Lettings</span><span>Managment</span><span>B.E.R.</span><span>Certs</span>
      </div>
      <div class="panel offer-panel">
        <h1 class="development-name">Verrow Gardens</h1>
        <p class="offer-sub">New exclusive 2 and 3 Bed Apartments</p>
        <h2 class="feature-headline">Luxuriously furnished and appointed.</h2>
        <p class="features">Dual Aspect to all apartments<br>2 secure Parking spaces per Apartment</p>
      </div>
      <div class="phone">362 4105</div>
      <div class="panel brand-panel">
        <p class="brand-name">TALLICK ESTATES</p>
        <p class="web-address">www.tallickestates-example.com</p>
      </div>
    </div>
  </div>
</body>
</html>
```